Copper lark buildworks

Copper lark buildworks is a small construction company.
Who is a licenced builder, Carpenter, joiner,
working on heritage ,new build, speacial projects and sometimes furniture

Industry/Entity Type

Construction

```html
<!DOCTYPE html>
<html lang="en">
<head>
<meta charset="utf-8">
<title>Copper lark buildworks – business cards</title>
<link rel="stylesheet" href="https://fonts.googleapis.com/css2?family=Source+Sans+3:wght@400;700&display=swap">
<style>
  :root {
    --page: #d9dad8;
    --card: #272727;
    --card-deep: #1a1a1a;
    --band: #0b0b0b;
    --green: #2bea4c;
    --green-mid: #18b23a;
    --green-dark: #0f7a28;
    --muted: #bdbdbd;
  }
  * { margin: 0; padding: 0; box-sizing: border-box; }
  html, body {
    width: 1200px; height: 900px; overflow: hidden;
    background: var(--page);
    font-family: "Source Sans 3", Arial, sans-serif;
  }
  .canvas { position: relative; width: 1200px; height: 900px; }
  .card {
    position: absolute;
    border-radius: 12px;
    overflow: hidden;
    box-shadow: 0 10px 24px rgba(0,0,0,.35);
  }
  .card svg.card-art { position: absolute; inset: 0; }
  .card-front { left: 258px; top: 183px; width: 445px; height: 292px; }
  .card-back  { left: 455px; top: 443px; width: 455px; height: 305px; }

  .brand {
    position: absolute;
    display: flex; align-items: center; gap: 8px;
    color: var(--green);
    font-weight: 700;
    white-space: nowrap;
  }
  .brand-square { width: 14px; height: 14px; background: var(--green); flex: none; }

  .card-front .brand { left: 0; right: 0; top: 165px; justify-content: center; font-size: 19px; }

  .card-back .brand-mark { left: 300px; top: 110px; font-size: 15px; }
  .card-back .brand-line {
    right: 210px; top: 214px;
    justify-content: flex-end;
    font-size: 13px; line-height: 1;
  }

  .person { position: absolute; left: 36px; top: 110px; color: var(--green); }
  .person-name { font-size: 17px; font-variant: small-caps; line-height: 1; letter-spacing: .3px; }
  .person-role { font-size: 12px; line-height: 1.2; }

  .contact {
    position: absolute; left: 168px; top: 237px;
    display: flex; align-items: center; gap: 9px;
    color: var(--muted); font-size: 11px; line-height: 1;
  }
  .contact svg { flex: none; }
</style>
</head>
<body>
<main class="canvas">

  <section class="card card-front" aria-label="Card front">
    <svg class="card-art" width="445" height="292" viewBox="0 0 445 292">
      <rect width="445" height="292" fill="var(--card)"/>
      <path d="M125 0 L320 0 Q372 146 320 292 L125 292 Q73 146 125 0 Z" fill="var(--card-deep)" stroke="#111" stroke-width="2"/>
      <path d="M96 70 Q80 146 96 222" fill="none" stroke="var(--green)" stroke-width="7" stroke-linecap="round"/>
      <path d="M349 50 Q366 130 352 212" fill="none" stroke="var(--green)" stroke-width="7" stroke-linecap="round"/>
    </svg>
    <div class="brand"><span class="brand-square"></span>Copper lark buildworks</div>
  </section>

  <section class="card card-back" aria-label="Card back">
    <svg class="card-art" width="455" height="305" viewBox="0 0 455 305">
      <rect width="455" height="305" fill="var(--card)"/>
      <rect x="0" y="102" width="280" height="42" fill="var(--band)"/>
      <path d="M300 0 H455 V305 H300 Q248 152 300 0 Z" fill="var(--card-deep)" stroke="#111" stroke-width="2"/>
      <path d="M264 55 Q246 148 276 232" fill="none" stroke="var(--green)" stroke-width="7" stroke-linecap="round"/>
      <rect x="292" y="210" width="55" height="30" fill="var(--green)"/>
      <rect x="347" y="210" width="55" height="30" fill="var(--green-mid)"/>
      <rect x="402" y="210" width="53" height="30" fill="var(--green-dark)"/>
    </svg>
    <div class="person">
      <p class="person-name">Miles Harlow</p>
      <p class="person-role">general manager</p>
    </div>
    <div class="brand brand-mark"><span class="brand-square"></span>Copper lark</div>
    <div class="brand brand-line">Copper lark buildworks</div>
    <div class="contact">
      <svg width="14" height="14" viewBox="0 0 14 14" aria-hidden="true">
        <circle cx="7" cy="7" r="7" fill="var(--green)"/>
        <path d="M4.6 3.5 L5.8 3.4 L6.4 5.2 L5.6 5.9 Q6.3 7.6 8 8.4 L8.7 7.6 L10.5 8.2 L10.4 9.4 Q9.8 10.3 8.6 10.1 Q4.2 9 3.9 4.6 Q3.9 3.8 4.6 3.5 Z" fill="#1a1a1a"/>
      </svg>
      <span>047 312 0946</span>
    </div>
  </section>

</main>
</body>
</html>
```